Geschäftspapiere für Hochzeits- und Event-DJ
Zielgruppe
Ich bin Hochzeits- und Event-DJ im Premiumsegment. Meine Zielgruppe sind Brautpaare und Firmen, denen gute Musik und gute Stimmung wichtig sind und die auch gerne bereit sind, dafür etwas mehr zu investieren. Weitere Info auf meiner Website: www.partyton-lindmark. de. An dies Farben der Website und des Logos soll das Design angelehnt sein.
Aufgabenstellung
Es sollte modern und hochwertig aussehen. Ich benötige eine Visitenkarte und Briefpapier für Rechnungen. Die Visitenkarte sollte beidseitig bedruckt sein. Auf der Visitenkarten benötige ich KEINE ADRESSDATEN. Nur Logo, mein Name und die Kontaktdaten (Mobil, Festnetz, E-Mail und Website). Auf dem Briefpapier sollen alle wichtigen Daten (inkl. Adresse, Steuernummer, Bankdaten, etc.) vorhanden sein. Die Visitenkarten sollte ein dunkles Design haben. Farben: Blau: R50 G170 B220 (#32aadc)
Grau: R50 G50 G50 (#323232)

```html
<!DOCTYPE html>
<html lang="de">
<head>
<meta charset="utf-8">
<title>Partyton Lindmark – Visitenkarte</title>
<link href="https://fonts.googleapis.com/css2?family=Open+Sans:wght@400;600;700&display=swap" rel="stylesheet">
<style>
  :root {
    --blue: #32aadc;
    --card: #1f1f20;
    --bg-light: #4a4a4a;
    --bg-dark: #262626;
    --text: #f2f2f2;
  }
  html, body {
    margin: 0;
    padding: 0;
    width: 1200px;
    height: 912px;
    overflow: hidden;
  }
  body {
    background: radial-gradient(ellipse at 50% 45%, var(--bg-light), var(--bg-dark));
    font-family: "Open Sans", Arial, sans-serif;
    position: relative;
  }
  .card {
    position: absolute;
    width: 640px;
    height: 366px;
    background: var(--card);
    box-shadow: 0 18px 40px rgba(0,0,0,.55);
    overflow: hidden;
  }
  .card::after {
    content: "";
    position: absolute;
    left: 0; right: 0; bottom: 0;
    height: 10px;
    background: var(--blue);
  }
  .card--front { left: 110px; top: 64px; }
  .card--back  { left: 450px; top: 478px; }

  .brand {
    display: flex;
    align-items: center;
    gap: 12px;
    color: var(--blue);
    font-weight: 700;
    font-size: 24px;
    letter-spacing: .3px;
  }
  .brand__dot {
    width: 26px; height: 26px;
    border-radius: 50%;
    background: var(--blue);
  }

  .card--front .brand {
    position: absolute;
    left: 0; right: 0; top: 120px;
    justify-content: center;
  }
  .card--front .site {
    position: absolute;
    left: 0; right: 0; top: 196px;
    text-align: center;
    color: var(--blue);
    font-size: 30px;
    font-weight: 400;
  }

  .card--back .brand {
    position: absolute;
    left: 60px; top: 168px;
    font-size: 20px;
  }
  .divider {
    position: absolute;
    left: 335px; top: 90px;
    width: 1.5px; height: 160px;
    background: var(--blue);
  }
  .contact {
    position: absolute;
    left: 360px; top: 92px;
  }
  .contact__company {
    margin: 0;
    color: var(--blue);
    font-weight: 700;
    font-size: 21px;
    line-height: 1.2;
  }
  .contact__name {
    margin: 2px 0 12px;
    color: var(--blue);
    font-weight: 600;
    font-size: 19px;
  }
  .contact__list {
    list-style: none;
    margin: 0; padding: 0;
    color: var(--text);
    font-size: 14px;
  }
  .contact__list li {
    display: flex;
    align-items: center;
    gap: 10px;
    line-height: 24px;
  }
  .contact__list svg {
    width: 14px; height: 14px;
    fill: none;
    stroke: var(--text);
    stroke-width: 1.6;
  }
</style>
</head>
<body>

<section class="card card--front">
  <div class="brand"><span class="brand__dot"></span>Partyton Lindmark</div>
  <div class="site">www.partyton-lindmark.de</div>
</section>

<section class="card card--back">
  <div class="brand"><span class="brand__dot"></span>Partyton Lindmark</div>
  <div class="divider"></div>
  <div class="contact">
    <p class="contact__company">Partyton Lindmark</p>
    <p class="contact__name">Jonas Weidner</p>
    <ul class="contact__list">
      <li>
        <svg viewBox="0 0 16 16"><path d="M3 2h3l1.5 3.5-2 1.2a8 8 0 0 0 3.8 3.8l1.2-2L14 10v3a1.5 1.5 0 0 1-1.5 1.5A11 11 0 0 1 1.5 3.5 1.5 1.5 0 0 1 3 2z"/></svg>
        +49 7000 4815162
      </li>
      <li>
        <svg viewBox="0 0 16 16"><rect x="4" y="1.5" width="8" height="13" rx="1.5"/><line x1="7" y1="12" x2="9" y2="12"/></svg>
        +49 150 0003427
      </li>
      <li>
        <svg viewBox="0 0 16 16"><rect x="1.5" y="3.5" width="13" height="9"/><path d="M1.5 3.5 8 9l6.5-5.5"/></svg>
        info@partyton-lindmark.de
      </li>
      <li>
        <svg viewBox="0 0 16 16"><circle cx="8" cy="8" r="6.5"/><path d="M1.5 8h13M8 1.5c2.5 2.5 2.5 10.5 0 13M8 1.5c-2.5 2.5-2.5 10.5 0 13"/></svg>
        www.partyton-lindmark.de
      </li>
    </ul>
  </div>
</section>

</body>
</html>
```